Trifold Business Brochure

We are looking to create a brochure for a company that does construction of oil and gas structures offshore and onshore. We need a brochure that closely mimics the the look and feel of the website - brelvo-works.com. You can pull text, photos, and anything else you need straight from the website. I have also uploaded zip file with many of the items that you may need for the development of the brochure.
We need to address all the pages that are in the website, but we only need a summary of the text (1-2 sentences or bullet points for services) for each area.

```html
<!DOCTYPE html>
<html lang="en">
<head>
<meta charset="utf-8">
<title>Brelvo Works – Trifold Brochure</title>
<link href="https://fonts.googleapis.com/css2?family=Montserrat:wght@400;700&display=swap" rel="stylesheet">
<style>
  :root {
    --panel: #231f20;
    --yellow: #f5e10a;
    --white: #ffffff;
    --frame: #ffffff;
    --seal: #111111;
    --badge-light: #f2f2f2;
    --badge-red: #c8202f;
    --badge-blue: #1f5fa8;
  }
  * { margin: 0; padding: 0; box-sizing: border-box; }
  html, body { width: 1200px; height: 927px; overflow: hidden; background: var(--panel); }
  .brochure {
    position: relative; width: 1200px; height: 927px;
    background: var(--panel); color: var(--white);
    font-family: "Montserrat", sans-serif;
  }
  .about { position: absolute; left: 46px; top: 46px; width: 312px; font-size: 15px; line-height: 15.2px; }
  .about h2 { color: var(--yellow); font-size: 15px; font-weight: 700; margin-bottom: 16px; }
  .about p { margin-bottom: 15.2px; }
  .about p.tight { margin-bottom: 0; }
  .contact {
    position: absolute; left: 450px; top: 238px; width: 300px;
    text-align: center; font-size: 13.8px; line-height: 16.5px;
  }
  .contact p { margin-bottom: 16.5px; }
  .badges { position: absolute; left: 444px; top: 488px; width: 312px; }
  .badge-row { display: flex; justify-content: center; align-items: center; gap: 16px; margin-bottom: 14px; }
  .badge { height: 28px; border-radius: 2px; }
  .badge.light { background: var(--badge-light); }
  .badge.red { background: var(--badge-red); border-radius: 6px; }
  .badge.blue { background: var(--badge-blue); }
  .hero-photo {
    position: absolute; left: 800px; top: 0; width: 400px; height: 618px;
    background: linear-gradient(180deg, #dcdfdf 0%, #c4c6bf 18%, #b8a85a 34%, #d0b22a 46%, #9b9680 58%, #4a5563 72%, #27323f 86%, #1a2430 100%);
  }
  .brand-seal {
    position: absolute; left: 880px; top: 335px; width: 238px; height: 238px;
    border-radius: 50%; background: var(--seal);
    display: flex; align-items: center; justify-content: center;
    color: var(--yellow); font-weight: 700; font-size: 32px; text-align: center; line-height: 36px;
  }
  .divider { position: absolute; left: 0; top: 618px; width: 1200px; height: 6px; background: var(--yellow); }
  .worker-photo {
    position: absolute; left: 0; top: 624px; width: 400px; height: 303px;
    background: linear-gradient(160deg, #a9ab97 0%, #8d8f63 22%, #b9c63a 40%, #6f6a5c 58%, #a39a88 76%, #c9c1b0 100%);
  }
  .map {
    position: absolute; left: 424px; top: 673px; width: 352px; height: 207px;
    border: 5px solid var(--frame);
    background: linear-gradient(180deg, #fbe80f 0%, #f5e10a 100%);
  }
  .services {
    position: absolute; left: 860px; top: 678px; width: 280px;
    text-align: center; color: var(--yellow); font-size: 18px; line-height: 22px;
  }
  .services h3 { font-size: 18px; font-weight: 700; }
  .services ul { list-style: none; margin-bottom: 22px; }
</style>
</head>
<body>
<div class="brochure">
  <section class="about">
    <h2>About Us</h2>
    <p>Brelvo Works has been in business since 1992, when it opened its first fabrication shop and offshore staging yard in Saltgrass Point, Louisiana with 15 employees.</p>
    <p>In 1994 the company opened its Harlow, Louisiana facility, which has grown to more then 200 employees. The Harlow facility has more than 20,000 square feet of fully equipped fabrication facilities, located on more than 10 acres of land that serve as staging and storage grounds.</p>
    <p>The main fabrication shop has two (2) 5-ton overhead cranes with 1-ton Jib cranes at the welding stations. The secondary fabrication shop is equipped with two (2) 10-ton overhead cranes and houses the Sub-Arc equipment. Both shops are capable to handle what ever size Piping or Structural component you require that can be transported by land. The company has added two additional divisions:</p>
    <p class="tight">Coded Vessels Department with the capability to fabricate new vessels and for the refurbishing and repair of used vessels.</p>
    <p class="tight">Production Operations Department with the capability to supply all of your Production personnel needs.</p>
  </section>

  <section class="contact">
    <p>Phone: 555-014-2800<br>Fax: 555-014-2811<br>Email: info@brelvo-works.com</p>
    <p>Physical Address:<br>2750 Harlow Rd.<br>Marsh Bend, LA 70999</p>
    <p>Mailing Address:<br>P.O. Box 40718<br>Cypress Reach, LA 70998</p>
    <p>www.brelvo-works.com</p>
  </section>

  <div class="badges" role="img" aria-label="Partner and certification badges">
    <div class="badge-row">
      <div class="badge light" style="width:102px;height:26px"></div>
      <div class="badge red" style="width:70px;height:32px"></div>
      <div class="badge light" style="width:102px"></div>
    </div>
    <div class="badge-row">
      <div class="badge light" style="width:80px;height:24px"></div>
      <div class="badge blue" style="width:94px;height:22px"></div>
    </div>
  </div>

  <div class="hero-photo" role="img" aria-label="Photo of an offshore oil and gas platform with yellow steel structures above the sea"></div>
  <div class="brand-seal">Brelvo<br>Works</div>

  <div class="divider"></div>

  <div class="worker-photo" role="img" aria-label="Photo of a construction worker in hard hat and safety vest measuring rebar in a foundation trench"></div>

  <div class="map" role="img" aria-label="Location map showing the facility on Harlow Rd. off Highway 90"></div>

  <section class="services">
    <h3>Onshore Services</h3>
    <ul>
      <li>Construction Services</li>
      <li>Fabrication Services</li>
      <li>Maintenance Services</li>
    </ul>
    <h3>Offshore Services</h3>
    <ul>
      <li>Construction Services</li>
      <li>Fabrication Services</li>
      <li>Maintenance Services</li>
    </ul>
  </section>
</div>
</body>
</html>
```